Business Card design for Founder and CEO of new shoe company

I am looking for a business card design for my new shoe company called Strido.

I am launching the company this April. Strido shoes offers slip-on athletic and casual style shoes for men and women. The unique selling point of the brand is that all of our shoe exist without shoelaces. I have included a link to the website to offer additional information about the company, see product images, and gain inspiration for the design. You can use the store owner password "Strido" to access the website.

www.Strido-shop.example

Thanks,
Dean Porlow

Target Market(s)

Active Men and Women ages 16-45

Industry/Entity Type

Business

Contact Information for Business Card

Dean Porlow
Founder and CEO
www.Strido-shop.example
deanporlow@Strido-shop.example
888-730-1964 / 888-7STRIDO
Strido, LLC
2384 N Tarrow St
Chicago, IL 60614

Requirements
Must have
• Be able to quickly and easily tell that Strido is a shoe company from the business card

```html
<!DOCTYPE html>
<html lang="en">
<head>
<meta charset="utf-8">
<title>Strido Business Card</title>
<link href="https://fonts.googleapis.com/css2?family=Questrial&display=swap" rel="stylesheet">
<style>
  :root {
    --page-white: #ffffff;
    --presentation-grey: #bbbcbe;
    --card-white: #ffffff;
    --ink: #231f20;
    --logo-ink: #2b2b2d;
    --asphalt-light: #5a5856;
    --asphalt-dark: #2e2d2c;
    --shoe-blue: #2f9fe0;
    --shoe-deep: #1d6fb0;
    --card-shadow: rgba(0, 0, 0, 0.45);
  }
  * { margin: 0; padding: 0; box-sizing: border-box; }
  html, body {
    width: 1200px;
    height: 1148px;
    overflow: hidden;
    background: var(--page-white);
  }
  body { font-family: "Questrial", "Century Gothic", sans-serif; color: var(--ink); }

  .presentation {
    position: absolute;
    left: 53px;
    top: 0;
    width: 1147px;
    height: 1148px;
    background: var(--presentation-grey);
  }

  .card {
    position: absolute;
    left: 217px;
    width: 820px;
    height: 467px;
    background: var(--card-white);
    box-shadow: 6px 7px 8px var(--card-shadow);
    overflow: hidden;
  }
  .card--front { top: 78px; }
  .card--back { top: 603px; }

  .asphalt-band {
    position: absolute;
    left: 0;
    right: 0;
    top: 340px;
    bottom: 0;
    background:
      radial-gradient(ellipse at 30% 40%, var(--asphalt-light), transparent 70%),
      linear-gradient(180deg, #4a4947, var(--asphalt-dark));
  }

  .brand-name {
    position: absolute;
    font-family: "Questrial", "Century Gothic", sans-serif;
    color: var(--logo-ink);
    font-weight: 400;
    letter-spacing: 1px;
    line-height: 1;
  }
  .card--front .brand-name {
    left: 28px;
    top: 36px;
    font-size: 66px;
  }
  .card--back .brand-name {
    left: 0;
    right: 0;
    top: 136px;
    text-align: center;
    font-size: 72px;
  }

  .contact-list {
    position: absolute;
    right: 31px;
    top: 27px;
    list-style: none;
    text-align: right;
    font-size: 20.5px;
    line-height: 25.3px;
  }

  .holder {
    position: absolute;
    left: 29px;
    top: 254px;
  }
  .holder__name {
    font-size: 34px;
    line-height: 1;
    font-weight: 400;
  }
  .holder__title {
    margin-top: 3px;
    font-size: 17px;
    line-height: 1;
  }

  .shoe-photo {
    position: absolute;
    left: 418px;
    top: 212px;
    width: 370px;
    height: 202px;
    border-radius: 40% 45% 20% 30% / 45% 50% 25% 30%;
    background: linear-gradient(160deg, var(--shoe-blue), var(--shoe-deep) 75%, #f2f2f2 92%);
  }

  .back-url {
    position: absolute;
    left: 0;
    right: 0;
    top: 259px;
    text-align: center;
    font-size: 19.5px;
  }
</style>
</head>
<body>
  <div class="presentation">
  </div>

  <section class="card card--front" aria-label="Business card front">
    <div class="brand-name">Strido</div>
    <ul class="contact-list">
      <li>www.Strido-shop.example</li>
      <li>deanporlow@Strido-shop.example</li>
      <li>888-730-1964</li>
      <li>888-7STRIDO</li>
      <li>Strido, LLC</li>
      <li>2384 N Tarrow St</li>
      <li>Chicago, IL 60614</li>
    </ul>
    <div class="holder">
      <h1 class="holder__name">Dean Porlow</h1>
      <p class="holder__title">Founder and CEO</p>
    </div>
    <div class="asphalt-band" role="img" aria-label="Asphalt road surface texture"></div>
    <div class="shoe-photo" role="img" aria-label="Photo of a blue and black laceless running shoe pair standing on asphalt"></div>
  </section>

  <section class="card card--back" aria-label="Business card back">
    <div class="brand-name">Strido</div>
    <p class="back-url">www.Strido-shop.example</p>
    <div class="asphalt-band" role="img" aria-label="Asphalt road surface texture"></div>
  </section>
</body>
</html>
```